the look of import selling star-up company

I have attached rhino logo that i like (can be edit) and i wanna turn that in to luxury look. Example like black base and gold logo +luxury looking font.

Company name: Vantel trading Oy
Slogan: Ordinary is not an option.
CEO Jarmo Keskinen
Starting to import ceramic nano coatings to cars, in home use and industrial purposes.

Target Market(s)

30-60 year old men and women ho have big money and know what car they drive

Industry/Entity Type

It Company

```html
<!DOCTYPE html>
<html lang="en">
<head>
<meta charset="utf-8">
<title>Vantel trading Oy — Business Card</title>
<link href="https://fonts.googleapis.com/css2?family=Open+Sans:wght@400;600&display=swap" rel="stylesheet">
<style>
  :root {
    --backdrop: #5a5a5a;
    --card-black: #141414;
    --card-black-edge: #0c0c0c;
    --gold: #c9a227;
    --gold-light: #e3c35a;
    --gold-dark: #9c7a17;
    --text-light: #e6e6e6;
    --text-muted: #bdbdbd;
    --band-text: #1a1406;
  }
  * { box-sizing: border-box; margin: 0; padding: 0; }
  html, body {
    width: 1200px;
    height: 904px;
    overflow: hidden;
    background: var(--backdrop);
    font-family: "Open Sans", Arial, sans-serif;
  }
  .sheet {
    width: 1200px;
    height: 904px;
    display: flex;
    flex-direction: column;
    align-items: center;
    justify-content: center;
    gap: 40px;
  }
  .card {
    position: relative;
    width: 680px;
    height: 388px;
    background: linear-gradient(160deg, var(--card-black) 0%, var(--card-black-edge) 100%);
    box-shadow: 0 10px 24px rgba(0,0,0,0.45);
    overflow: hidden;
  }

  /* Front */
  .card--front {
    display: flex;
    flex-direction: column;
    align-items: center;
    justify-content: center;
  }
  .brand-dot {
    width: 118px;
    height: 118px;
    border-radius: 50%;
    background: var(--gold);
    margin-bottom: 22px;
  }
  .brand-name {
    color: var(--gold);
    font-weight: 600;
    font-size: 34px;
    letter-spacing: 0.5px;
    line-height: 1.1;
  }
  .brand-slogan {
    margin-top: 6px;
    color: var(--text-muted);
    font-size: 15px;
    letter-spacing: 1px;
  }

  /* Back */
  .contact-block {
    position: absolute;
    top: 118px;
    left: 0;
    right: 0;
    display: flex;
    justify-content: center;
    align-items: center;
    gap: 20px;
  }
  .person {
    text-align: right;
  }
  .person-name {
    color: var(--text-light);
    font-size: 24px;
    font-weight: 400;
    letter-spacing: 0.5px;
  }
  .person-role {
    color: var(--text-muted);
    font-size: 15px;
    margin-top: 2px;
  }
  .divider {
    width: 1px;
    height: 72px;
    background: var(--text-muted);
  }
  .contacts {
    list-style: none;
    display: flex;
    flex-direction: column;
    gap: 5px;
  }
  .contact-item {
    display: flex;
    align-items: center;
    gap: 10px;
    color: var(--text-light);
    font-size: 15px;
  }
  .contact-icon {
    width: 14px;
    height: 14px;
    flex: none;
  }
  .tagline-band {
    position: absolute;
    left: 0;
    right: 0;
    top: 300px;
    height: 30px;
    background: linear-gradient(90deg, var(--gold-dark) 0%, var(--gold-light) 45%, var(--gold) 100%);
    display: flex;
    align-items: center;
    justify-content: center;
  }
  .tagline {
    color: var(--band-text);
    font-size: 15px;
    letter-spacing: 0.3px;
  }
</style>
</head>
<body>
  <main class="sheet">
    <section class="card card--front" aria-label="Card front">
      <div class="brand-dot" aria-hidden="true"></div>
      <h1 class="brand-name">Vantel trading Oy</h1>
      <p class="brand-slogan">Ordinary is not an option</p>
    </section>

    <section class="card card--back" aria-label="Card back">
      <div class="contact-block">
        <div class="person">
          <p class="person-name">Jarmo Keskinen</p>
          <p class="person-role">CEO</p>
        </div>
        <div class="divider" aria-hidden="true"></div>
        <ul class="contacts">
          <li class="contact-item">
            <svg class="contact-icon" viewBox="0 0 16 16" aria-hidden="true">
              <path d="M3.5 1.5l2.5 0 1.2 3.2-1.6 1.2a8 8 0 0 0 4.5 4.5l1.2-1.6 3.2 1.2v2.5a1.5 1.5 0 0 1-1.6 1.5A12.5 12.5 0 0 1 2 3.1 1.5 1.5 0 0 1 3.5 1.5z" fill="var(--gold)"/>
            </svg>
            +358 40 555 0182
          </li>
          <li class="contact-item">
            <svg class="contact-icon" viewBox="0 0 16 16" aria-hidden="true">
              <rect x="1" y="3" width="14" height="10" rx="1.5" fill="var(--gold)"/>
              <path d="M1.5 4l6.5 5 6.5-5" fill="none" stroke="var(--card-black)" stroke-width="1.3"/>
            </svg>
            info@vanteltrading.fi
          </li>
          <li class="contact-item">
            <svg class="contact-icon" viewBox="0 0 16 16" aria-hidden="true">
              <circle cx="8" cy="8" r="6.8" fill="none" stroke="var(--gold)" stroke-width="1.4"/>
              <ellipse cx="8" cy="8" rx="3" ry="6.8" fill="none" stroke="var(--gold)" stroke-width="1.2"/>
              <path d="M1.2 8h13.6M2.5 4.5h11M2.5 11.5h11" stroke="var(--gold)" stroke-width="1.1"/>
            </svg>
            www.vanteltrading.fi
          </li>
        </ul>
      </div>
      <div class="tagline-band">
        <p class="tagline">Starting to import ceramic nano coatings to cars, in home use and industrial purposes.</p>
      </div>
    </section>
  </main>
</body>
</html>
```